Brell Harbor Company Business Cards

Front and Back Business Card - logo and text setup - cool design. I need workable photoshop or illustrator files so I can setup each employee card with design that is created
Updates

Hi everyone, thank you for the great entries. Please no more white and blue cards - there are so many already - black and silver only now please. thanks!

Target Market(s)

Construction Industry - Facility Managers

Industry/Entity Type

Construction

Contact Information for Business Card

I really like contemporary simplistic looks - clean neat....not opposed to seeing some black backrounds

Requirements
Must have
• Logo/website address with design on front only - www.brellharbor-example.com (logo attached)
• Back:
• Name/Title/Company Address/Phone/email address
Nice to have
• Cool design
Should not have
• Nothing gimmicky like Fire or Water - since we are a Fire Protection company - it has all been done

```html
<!DOCTYPE html>
<html lang="en">
<head>
<meta charset="utf-8">
<title>Brell Harbor Company Business Cards</title>
<link rel="stylesheet" href="https://fonts.googleapis.com/css2?family=Montserrat:wght@400;500;800&display=swap">
<style>
  :root {
    --backdrop: #5b5b5e;
    --black: #111112;
    --black-soft: #2a2a2c;
    --silver-light: #e9e9ec;
    --silver: #c4c5c9;
    --silver-mid: #9c9da2;
    --silver-dark: #6f7075;
    --graphite: #3a3a3d;
  }
  * { box-sizing: border-box; margin: 0; padding: 0; }
  html, body { width: 1200px; height: 866px; overflow: hidden; }
  body {
    background: var(--backdrop);
    font-family: "Montserrat", Arial, sans-serif;
    position: relative;
  }
  .card {
    position: absolute;
    width: 560px;
    height: 320px;
    box-shadow: 0 14px 30px rgba(0,0,0,0.4);
    overflow: hidden;
  }

  /* Contact side: brushed silver */
  .card-contact {
    left: 70px;
    top: 80px;
    background: linear-gradient(135deg, var(--silver-light) 0%, var(--silver) 55%, #d8d9dc 100%);
  }
  .brand-name {
    position: absolute;
    left: 36px;
    top: 42px;
    font-weight: 800;
    font-size: 34px;
    letter-spacing: -0.5px;
    color: var(--black);
  }
  .name-row {
    position: absolute;
    left: 36px;
    right: 36px;
    top: 118px;
    display: flex;
    align-items: flex-end;
    gap: 10px;
  }
  .square-row { flex: none; display: block; }
  .person { text-align: left; }
  .person-name {
    font-weight: 500;
    font-size: 24px;
    color: var(--black);
    line-height: 1;
    white-space: nowrap;
  }
  .person-title {
    font-size: 14px;
    color: var(--graphite);
    margin-top: 4px;
  }
  .address {
    position: absolute;
    right: 36px;
    top: 190px;
    text-align: right;
    font-size: 12.5px;
    line-height: 1.5;
    color: var(--graphite);
  }
  .contact-lines {
    position: absolute;
    left: 36px;
    bottom: 32px;
    font-size: 13px;
    color: var(--graphite);
    line-height: 1.9;
  }
  .contact-line { display: flex; align-items: center; gap: 10px; }
  .contact-line svg { width: 13px; height: 13px; flex: none; }

  /* Logo side: black */
  .card-brand {
    left: 570px;
    top: 470px;
    background: radial-gradient(ellipse at 30% 20%, var(--black-soft), var(--black) 80%);
    display: flex;
    flex-direction: column;
    align-items: center;
    justify-content: center;
    gap: 18px;
  }
  .brand-mark {
    display: flex;
    align-items: center;
    gap: 12px;
  }
  .brand-mark-square {
    width: 14px;
    height: 14px;
    background: var(--silver);
  }
  .brand-mark-name {
    font-weight: 800;
    font-size: 50px;
    letter-spacing: -1px;
    color: var(--silver);
  }
  .website {
    font-weight: 500;
    font-size: 15px;
    letter-spacing: 1.5px;
    color: var(--silver);
  }
</style>
</head>
<body>

<section class="card card-contact" aria-label="Business card, contact side">
  <div class="brand-name">Brell Harbor</div>

  <div class="name-row">
    <svg class="square-row" width="300" height="16" viewBox="0 0 300 16" aria-hidden="true">
      <rect x="0"   y="5" width="12" height="10" fill="#b9babe"/>
      <rect x="20"  y="5" width="12" height="10" fill="#b2b3b7"/>
      <rect x="40"  y="4" width="13" height="11" fill="#aaabb0"/>
      <rect x="60"  y="4" width="13" height="11" fill="#a1a2a7"/>
      <rect x="80"  y="4" width="13" height="11" fill="#98999e"/>
      <rect x="100" y="3" width="14" height="12" fill="#8e8f94"/>
      <rect x="120" y="3" width="14" height="12" fill="#84858a"/>
      <rect x="140" y="3" width="14" height="12" fill="#797a7f"/>
      <rect x="160" y="2" width="15" height="13" fill="#6e6f74"/>
      <rect x="180" y="2" width="15" height="13" fill="#626367"/>
      <rect x="200" y="2" width="15" height="13" fill="#55565a"/>
      <rect x="220" y="1" width="16" height="14" fill="#48494c"/>
      <rect x="240" y="1" width="16" height="14" fill="#3a3a3d"/>
      <rect x="260" y="0" width="17" height="15" fill="#2a2a2c"/>
      <rect x="282" y="0" width="17" height="15" fill="#111112"/>
    </svg>
    <div class="person">
      <div class="person-name">Dana Reyes</div>
      <div class="person-title">Manager</div>
    </div>
  </div>

  <div class="address">
    48 Quarry Lane<br>
    Millbrook, AB, T2K 4R8
  </div>

  <div class="contact-lines">
    <div class="contact-line">
      <svg viewBox="0 0 24 24" aria-hidden="true"><path fill="#111112" d="M6.6 10.8a15.1 15.1 0 0 0 6.6 6.6l2.2-2.2c.3-.3.7-.4 1-.2 1.1.4 2.3.6 3.6.6.6 0 1 .4 1 1V20c0 .6-.4 1-1 1A17 17 0 0 1 3 4c0-.6.4-1 1-1h3.5c.6 0 1 .4 1 1 0 1.3.2 2.5.6 3.6.1.3 0 .7-.2 1z"/></svg>
      <span>555-014-2283</span>
    </div>
    <div class="contact-line">
      <svg viewBox="0 0 24 24" aria-hidden="true"><rect x="2" y="5" width="20" height="14" fill="#111112"/><path d="M2 5l10 8 10-8" fill="none" stroke="#d8d9dc" stroke-width="1.8"/></svg>
      <span>dana.reyes@brellharbor-example.com</span>
    </div>
  </div>
</section>

<section class="card card-brand" aria-label="Business card, logo side">
  <div class="brand-mark">
    <span class="brand-mark-square" aria-hidden="true"></span>
    <span class="brand-mark-name">Brell Harbor</span>
  </div>
  <div class="website">www.brellharbor-example.com</div>
</section>

</body>
</html>
```